I need creative and unique business card design using my company logo. Ok to change logo color. We are a small brokerage doing both Real Estate and Mortgage services. Need to have the follow on business card;
1. agent name - Nora Velden - Realtor
2. cell - 949-555-0182
3. license number - DRE 07164392
4. business name - Bright Keys & Lending, Inc
5. business office - 626-555-0147
6. business address - 214 W. Marlowe Ave #308, Arcadia CA 91006
7. business logo - attached (ok to use different color on logo)

```html
<!DOCTYPE html>
<html lang="en">
<head>
<meta charset="utf-8">
<title>Bright Keys &amp; Lending, Inc — Business Card</title>
<link rel="stylesheet" href="https://fonts.googleapis.com/css2?family=Montserrat:wght@400;500;700&display=swap">
<style>
  :root {
    --backdrop: #8c735a;
    --card-white: #ffffff;
    --brand-deep: #2a5aa6;
    --brand-mid: #3a78bf;
    --brand-light: #4b9bd8;
    --ink: #1c1c1c;
    --on-blue: #ffffff;
  }
  * { margin: 0; padding: 0; box-sizing: border-box; }
  html, body { width: 900px; height: 1200px; overflow: hidden; }
  body {
    position: relative;
    background: var(--backdrop);
    font-family: "Montserrat", sans-serif;
    color: var(--ink);
  }
  .card {
    position: absolute;
    left: 68px;
    width: 758px;
    height: 440px;
    border-radius: 28px;
    overflow: hidden;
    box-shadow: 0 6px 14px rgba(0,0,0,0.35);
  }
  .card--front { top: 133px; background: var(--card-white); }
  .card--back {
    top: 638px;
    height: 442px;
    background: linear-gradient(90deg, var(--brand-deep), var(--brand-light));
  }

  .wordmark { position: absolute; color: var(--brand-deep); font-weight: 500; }
  .wordmark__name { display: block; font-size: 33px; letter-spacing: 0.3em; line-height: 1; }
  .wordmark__sub { display: block; font-size: 15.5px; letter-spacing: 0.14em; line-height: 1; margin-top: 8px; }
  .card--front .wordmark { left: 29px; top: 64px; }

  .agent { position: absolute; right: 44px; top: 55px; text-align: right; }
  .agent__name { font-size: 23px; font-weight: 700; color: var(--brand-deep); line-height: 1.2; }
  .agent__name span { color: var(--brand-light); }
  .agent__title { font-size: 16px; font-weight: 500; margin-top: 6px; }
  .accent-tab {
    position: absolute; right: 0; top: 59px;
    width: 12px; height: 46px; background: var(--brand-mid);
  }

  .brand-square {
    position: absolute; left: 480px; top: 182px;
    width: 249px; height: 238px;
    background: linear-gradient(180deg, var(--brand-deep) 0%, var(--brand-light) 45%, var(--brand-deep) 100%);
  }

  .address { position: absolute; left: 32px; top: 232px; font-size: 16px; line-height: 20px; }
  .contact { position: absolute; left: 32px; top: 323px; list-style: none; font-size: 16px; }
  .contact li { display: flex; align-items: center; height: 25px; }
  .contact svg { width: 16px; height: 18px; margin-right: 14px; fill: var(--brand-deep); }
  .license { position: absolute; left: 34px; top: 389px; font-size: 16px; }

  .card--back .brand-square-mark {
    position: absolute; left: 318px; top: 117px;
    width: 141px; height: 137px; background: var(--on-blue);
  }
  .card--back .wordmark {
    left: 0; right: 0; top: 285px; text-align: center; color: var(--on-blue);
  }
  .card--back .wordmark__name { padding-left: 0.3em; }
</style>
</head>
<body>
  <section class="card card--front" aria-label="Card front">
    <div class="wordmark">
      <span class="wordmark__name">BRIGHT KEYS</span>
      <span class="wordmark__sub">&amp; LENDING, INC</span>
    </div>

    <div class="agent">
      <p class="agent__name">Nora <span>Velden</span></p>
      <p class="agent__title">Realtor</p>
    </div>
    <div class="accent-tab"></div>

    <p class="address">214 W. Marlowe Ave #308,<br>Arcadia CA 91006</p>

    <ul class="contact">
      <li>
        <svg viewBox="0 0 16 18" aria-hidden="true"><path d="M1 6c0-3 3-4 7-4s7 1 7 4v1h-4V5H5v2H1zM3 8h10l2 8H1z"/></svg>
        626-555-0147
      </li>
      <li>
        <svg viewBox="0 0 16 18" aria-hidden="true"><path d="M4 0h8a2 2 0 0 1 2 2v14a2 2 0 0 1-2 2H4a2 2 0 0 1-2-2V2a2 2 0 0 1 2-2zm0 2v12h8V2zm4 13a1 1 0 1 0 0 2 1 1 0 0 0 0-2z"/></svg>
        949-555-0182
      </li>
    </ul>

    <p class="license">License number - DRE 07164392</p>

    <div class="brand-square"></div>
  </section>

  <section class="card card--back" aria-label="Card back">
    <div class="brand-square-mark"></div>
    <div class="wordmark">
      <span class="wordmark__name">BRIGHT KEYS</span>
      <span class="wordmark__sub">&amp; LENDING, INC</span>
    </div>
  </section>
</body>
</html>
```